Flyer für einen Sanitär Heizungs Betrieb
Zielgruppe
Sanitär Heizungs Betrieb der den Fokus verstärkt auf den Service an Heizungsanlagen setzten will.
Der Flyer soll sowohl an Privathaushalte als auch an Hausverwaltungen gehen.
Er soll unsere Leistungen aufzeigen und einen guten ersten Eindruck vermitteln.
Aufgabenstellung
Anbei sende ich Themen die als Leistung aufgeführt werden, sowie Strichwort für einen Werbetext (kann gerne generiert werden ansonsten kommt er noch zum texter)

```html
<!DOCTYPE html>
<html lang="de">
<head>
<meta charset="UTF-8">
<title>Nordwärm GmbH – Flyer</title>
<link rel="stylesheet" href="https://fonts.googleapis.com/css2?family=Open+Sans:wght@300;400;600;700&display=swap">
<style>
  :root {
    --white: #ffffff;
    --ink: #1d1d1b;
    --accent-yellow: #f4c32c;
    --accent-blue: #1a73bf;
    --brand-red: #e2231a;
  }
  * { margin: 0; padding: 0; box-sizing: border-box; }
  html, body { width: 848px; height: 1200px; overflow: hidden; background: var(--white); }
  body { font-family: "Open Sans", Arial, sans-serif; color: var(--ink); }

  .flyer { position: relative; width: 848px; height: 1200px; overflow: hidden; }

  .hero { position: absolute; left: 0; top: 0; width: 848px; height: 536px; }
  .hero-photo {
    position: absolute; inset: 0;
    background:
      linear-gradient(180deg, rgba(20,24,26,0.55) 0%, rgba(20,24,26,0.62) 60%, rgba(20,24,26,0.45) 100%),
      linear-gradient(180deg, #6f7a80 0%, #8d9498 35%, #9aa09f 60%, #4d5a3c 85%, #3e4d2e 100%);
  }

  .brand-box {
    position: absolute; left: 581px; top: 41px; width: 264px; height: 118px;
    background: var(--white);
    display: flex; align-items: center; justify-content: center; gap: 10px;
  }
  .brand-mark { width: 18px; height: 18px; background: var(--brand-red); }
  .brand-name { font-weight: 700; font-size: 24px; color: var(--brand-red); letter-spacing: 0.3px; }

  .hero-title {
    position: absolute; left: 50px; top: 167px; width: 560px;
    color: var(--white); font-weight: 700; font-size: 35px; line-height: 46px;
    text-transform: uppercase; letter-spacing: 0.3px; white-space: nowrap;
  }
  .hero-rule {
    position: absolute; left: 50px; top: 334px; width: 218px; height: 4px;
    background: var(--accent-yellow);
  }
  .hero-intro {
    position: absolute; left: 50px; top: 372px; width: 620px;
    color: var(--accent-yellow); font-weight: 700; font-size: 21px; line-height: 28.5px;
    text-align: justify;
  }

  .services { position: absolute; left: 50px; top: 562px; width: 760px; }
  .services-title {
    color: var(--accent-blue); font-weight: 600; font-size: 29.5px; line-height: 38px;
    margin-bottom: 23px; letter-spacing: 0.2px;
  }
  .service-list { list-style: none; }
  .service-item {
    font-weight: 300; font-size: 19.5px; line-height: 25.5px; margin-bottom: 24.5px;
    color: var(--ink); white-space: nowrap;
  }
  .service-label { font-weight: 700; }
</style>
</head>
<body>
<div class="flyer">
  <header class="hero">
    <div class="hero-photo" role="img" aria-label="Foto eines modernen Einfamilienhauses mit Wärmepumpe im Garten, dunkel abgetönt"></div>
    <div class="brand-box">
      <span class="brand-mark"></span>
      <span class="brand-name">Nordwärm GmbH</span>
    </div>
    <h1 class="hero-title">Herzlich willkommen<br>bei Nordwärm – Ihrem<br>Heizungsbetrieb</h1>
    <div class="hero-rule"></div>
    <p class="hero-intro">Hier sind Sie richtig, wenn Sie nach einem erfahrenen und zuverlässigen Service von Nordwärm mit Kompetenz in Heizung, Badsanierung, Brennstoff­zellenheizung und Wärmepumpen suchen!</p>
  </header>

  <section class="services">
    <h2 class="services-title">UNSERE LEISTUNGEN FÜR SIE</h2>
    <ul class="service-list">
      <li class="service-item"><span class="service-label">NOTDIENST HEIZUNG:</span> Soforthilfe im Notfall für Heizungsprobleme</li>
      <li class="service-item"><span class="service-label">SOLARANLAGENSERVICE:</span> Spülen und Entlüften von Solaranlagen</li>
      <li class="service-item"><span class="service-label">WARTUNG:</span> Allgemeine Heizungsdienstleistungen für Öl, Gas, Solaranla-<br>gen, Wärmepumpen und Gasgeräte</li>
      <li class="service-item"><span class="service-label">STÖRUNGSBESEITIGUNG:</span> Reparaturen und Problemlösungen für<br>Heizungs- und Sanitäranlagen</li>
      <li class="service-item"><span class="service-label">WASSERQUALITÄTSTEST:</span> Prüfung und Aufbereitung des Heizungswas-<br>sers nach VDI 123 Standard</li>
      <li class="service-item"><span class="service-label">HEIZUNGSANLAGENSPÜLUNG:</span> Reinigung von Fußbodenheizungen<br>durch Spülen der Heizungsanlagen</li>
      <li class="service-item"><span class="service-label">FLEXIBLE HILFE:</span> Schnelle, unkomplizierte Unterstützung bei verschiede-<br>nen Anliegen</li>
      <li class="service-item"><span class="service-label">AUSTAUSCH &amp; MODERNISIERUNG:</span> Erneuerung und zeitgemäße Moder-<br>nisierung von Heizungsanlagen</li>
    </ul>
  </section>
</div>
</body>
</html>
```